Revelation Sanctuary Flyer

We need a flyer for a church seminar that focuses on the Revelation and the sanctuary, it will show images with giants, UFOs maybe some pyramids, sanctuary furniture pieces.

Front Cover, Middle and Back cover. size 8.5 x 11 folded in the middle
The information is in file 1 and file 2.
The other files are examples and ideas for layout.

Target Market(s)

Churches

Requirements
Must have
• 1. Flyer design files have to be print ready.
• 2. Must have appropriate bleed size and safe zone
• PDF, JPEG, PSD, AI, TIFF
Nice to have
• Images of Giants, UFO, Sanctuary building, Pyramids

```html
<!DOCTYPE html>
<html lang="en">
<head>
<meta charset="utf-8">
<title>Revelation Sanctuary Flyer</title>
<link href="https://fonts.googleapis.com/css2?family=Merriweather:ital,wght@0,400;0,700;0,900;1,400;1,700&family=Oswald:wght@500;600&family=Roboto:ital,wght@0,400;0,500;0,700;1,700&display=swap" rel="stylesheet">
<style>
:root{
  --rust:#a6513a;
  --rust-text:#a84f33;
  --blush:#f5dcd4;
  --card-pink:#e9b3a1;
  --yellow:#ffe01a;
  --charcoal:#2f2e2a;
  --ink:#2a2a2a;
  --white:#ffffff;
  --page:#f4f1ec;
}
*{margin:0;padding:0;box-sizing:border-box}
html,body{width:900px;height:1200px;overflow:hidden;background:var(--page)}
body{position:relative;font-family:'Roboto',Arial,sans-serif;color:var(--ink)}
.sheet-label{position:absolute;font-size:15px;color:#222;font-family:'Roboto',Arial,sans-serif}
.spread{position:absolute;left:90px;width:720px;height:555px;overflow:hidden}
.spread--outer{top:34px}
.spread--inside{top:622px;background:#f8ece7}
.panel{position:absolute;top:0;width:360px;height:555px;overflow:hidden}
.panel--back{left:0;background:var(--blush)}
.panel--front{left:360px}
.photo{position:absolute}

/* back cover */
.invite-head{position:absolute;left:23px;top:16px;font-family:'Merriweather',Georgia,serif;font-weight:700;color:var(--rust-text);line-height:1.02;z-index:1}
.invite-head .big{font-size:29px;display:block;line-height:1.08}
.invite-head .mid{font-size:21px;display:block;line-height:1.22}
.why-box{position:absolute;left:17px;top:214px;width:343px;height:51px;background:var(--white);padding:6px 8px}
.why-box h3{font-size:13.5px;font-weight:700;color:var(--rust-text);margin-bottom:4px}
.why-box p{font-size:7.6px;line-height:1.35;color:#555}
.question-band{position:absolute;left:0;top:271px;width:360px;height:114px;background:var(--rust)}
.question-band .ask{position:absolute;left:22px;top:6px;width:140px;font-family:'Merriweather',Georgia,serif;font-weight:700;font-size:13.4px;line-height:1.55;color:var(--yellow)}
.question-band .answers{position:absolute;left:160px;top:6px;width:170px}
.answers h4{font-size:8.4px;font-style:italic;font-weight:700;color:var(--yellow);margin-bottom:4px;white-space:nowrap}
.answers ul{list-style:none}
.answers li{position:relative;padding-left:12px;font-size:7.5px;line-height:1.4;color:var(--white)}
.answers li::before{content:"";position:absolute;left:2px;top:4px;width:3px;height:3px;border-radius:50%;background:var(--yellow)}
.location{position:absolute;left:24px;top:398px;width:150px;font-size:7.8px;line-height:1.3;color:#333}
.location h4{font-size:10px;font-weight:700;color:var(--rust-text)}
.location .org{font-weight:700;color:var(--rust-text)}
.location .small{font-size:6.4px}
.location .pastor{margin-top:12px;font-weight:700;color:var(--rust-text)}
.location b{font-weight:700}
.map{position:absolute;left:172px;top:396px;width:162px;height:114px;background:linear-gradient(135deg,#f3e2dc,#e7d0c8);border:1px solid #d7bdb3}
.free-row{position:absolute;left:0;top:515px;width:360px;height:16px;background:var(--white);display:flex;font-size:7.8px;align-items:center}
.free-row span{padding:0 8px 0 22px;border-right:3px solid var(--blush)}
.free-row span:first-child{padding-left:24px}
.free-row span:last-child{border-right:none}
.free-row b{color:var(--rust-text);font-weight:700}
.stream{position:absolute;left:0;top:533px;width:360px;text-align:center;font-size:8.2px;font-weight:700;color:#333}

/* front cover */
.cover-title{position:absolute;left:180px;top:152px;width:180px;font-family:'Oswald','Arial Narrow',sans-serif;font-weight:600;color:var(--yellow);line-height:1.05;text-transform:uppercase;white-space:nowrap}
.cover-title .presents{font-size:14px;display:block;line-height:1.02}
.cover-title .presents + .presents{margin-bottom:6px}
.cover-title .main{display:block;letter-spacing:-0.5px}
.cover-title .t1{font-size:32px}
.cover-title .t2{font-size:24px}
.cover-title .t3{font-size:26px}
.cover-title .t4{font-size:30px}
.date-strip{position:absolute;left:0;top:525px;width:360px;height:15px;background:var(--white);text-align:center;font-size:9px;font-weight:700;line-height:15px;color:#222}

/* inside */
.inside-shapes{position:absolute;left:0;top:0}
.headline{position:absolute;left:292px;top:26px;font-family:'Merriweather',Georgia,serif;font-weight:900;font-size:30px;line-height:1.12;color:var(--yellow);white-space:nowrap}
.subhead{position:absolute;left:433px;top:104px;width:270px;font-family:'Merriweather',Georgia,serif;font-weight:700;font-size:11.5px;line-height:1.35;color:var(--yellow);white-space:nowrap}
.family-invite{position:absolute;left:230px;top:156px;width:420px;text-align:center;font-family:'Merriweather',Georgia,serif;font-weight:700;font-size:13px;line-height:1.55;color:#f2ebe0}
.session{position:absolute;top:200px;width:161px;height:185px;background:var(--card-pink);border-radius:7px;overflow:hidden}
.session .head{position:absolute;left:0;top:0;width:161px;height:44px;background:#f8e4dc;clip-path:polygon(0 0,82% 0,100% 30%,100% 100%,0 100%)}
.session h5{position:absolute;left:0;top:7px;width:161px;text-align:center;font-size:17px;font-weight:400;color:#222;letter-spacing:-0.2px}
.session h5 b{font-weight:700}
.session .when{position:absolute;left:0;top:29px;width:161px;text-align:center;font-size:7.6px;font-weight:700;color:#222}
.session .frame{position:absolute;left:9px;top:45px;width:152px;height:95px;background:var(--rust)}
.session .pic{position:absolute;left:12px;top:45px;width:116px;height:93px}
.session .label{position:absolute;left:0;top:144px;width:161px;text-align:center;font-size:19px;line-height:1;color:#3b2b27}
.session--one{left:187px}.session--two{left:363px}.session--three{left:540px}
.speaker{position:absolute;left:24px;top:344px;width:158px}
.speaker h3{font-family:'Merriweather',Georgia,serif;font-weight:700;font-size:14.5px;color:var(--rust-text);margin-bottom:4px}
.speaker p{font-family:'Merriweather',Georgia,serif;font-size:8.9px;line-height:1.36;color:#222}
.speaker p i{font-weight:700}
.feature{position:absolute;left:187px;width:161px;height:35px;background:var(--rust);border-bottom:3px solid #6d3021;display:flex;align-items:center;justify-content:center;text-align:center;font-family:'Merriweather',Georgia,serif;font-weight:900;font-size:12.4px;line-height:1.1;color:var(--yellow)}
.topics{position:absolute;left:366px;top:403px;width:336px;background:var(--white);border:1px solid var(--rust)}
.topics h4{height:19px;background:var(--rust);color:var(--yellow);font-family:'Merriweather',Georgia,serif;font-weight:900;font-size:13px;letter-spacing:4px;text-align:center;line-height:19px}
.topics table{width:100%;border-collapse:collapse;table-layout:fixed}
.topics td{width:33.3%;padding:2px 4px;font-size:6.8px;line-height:1.15;border-right:1px solid #c98d7b;border-bottom:1px solid #c98d7b;vertical-align:top;height:27px}
.topics td:last-child{border-right:none}
.topics tr:last-child td{border-bottom:none}
.topics td b{display:block;font-weight:700}
</style>
</head>
<body>

<div class="sheet-label" style="left:235px;top:10px">Back</div>
<div class="sheet-label" style="left:595px;top:10px">Front</div>

<section class="spread spread--outer">
  <div class="panel panel--back">
    <div class="photo" role="img" aria-label="Photo of a troubled man leaning his head on his hand beside a glass" style="left:230px;top:70px;width:130px;height:144px;background:linear-gradient(160deg,#c9aaa2 0%,#5c4e4c 45%,#3d3534 100%)"></div>
    <h1 class="invite-head">
      <span class="big">We invite you<br>to come as you are</span>
      <span class="mid">And discover hope<br>&amp; lasting peace<br>in these<br>trouble times</span>
    </h1>
    <div class="why-box">
      <h3>Why Study Revelation?</h3>
      <p>Blessed is he who reads and those who hear the words of this prophecy, and<br>keep those things which are written in it; for the time is near. Revelation 1:3</p>
    </div>
    <div class="question-band">
      <p class="ask">If you have a<br>plaguing question,<br>submit it<br>and we will<br>answer it.......</p>
      <div class="answers">
        <h4>Find answers to your everyday questions:</h4>
        <ul>
          <li>What does the Bible say about the end of the world?</li>
          <li>Were there really Giants in the world?</li>
          <li>Are there UFO's?</li>
          <li>Why is there so much pain and suffering in the world?</li>
          <li>Is there life after death?</li>
          <li>Is Heaven and Hell real?</li>
        </ul>
      </div>
    </div>
    <div class="location">
      <h4>MEETING LOCATION</h4>
      <div class="org">Bethany Grove SDA Church</div>
      <div>2870 Linden Ave</div>
      <div>Brookfield, NY 11000</div>
      <div class="small">(corner of Linden Ave &amp; Harlow Rd)</div>
      <div><b>Phone:</b> 555-201-4480</div>
      <div class="pastor">Dr. Marcus L. Hale, Pastor</div>
      <div><b>Phone:</b> 555-318-2074</div>
    </div>
    <div class="map" role="img" aria-label="Street map showing the church location"></div>
    <div class="free-row">
      <span><b>FREE</b> Admission</span>
      <span><b>FREE</b> Study Guides</span>
      <span><b>FREE</b> Books</span>
      <span><b>FREE</b> Health Materials</span>
    </div>
    <p class="stream">Streaming live at: www.bethanygrovesda.org/resources/watch-us-live</p>
  </div>

  <div class="panel panel--front">
    <div class="photo" role="img" aria-label="Collage of a floating pyramid, standing stones, sanctuary furniture and a dark giant silhouette under a dusky sky" style="left:0;top:0;width:360px;height:555px;background:linear-gradient(180deg,#58507a 0%,#b9898a 30%,#d59a78 45%,#6d5a3e 65%,#4e4a2c 85%,#3a3424 100%)"></div>
    <div class="photo" role="img" aria-label="Silhouette of a giant figure" style="left:165px;top:20px;width:195px;height:535px;background:linear-gradient(180deg,#3b3923,#2c2b1d);border-radius:70px 20px 0 0;opacity:.92"></div>
    <h2 class="cover-title">
      <span class="presents">Bethany Grove SDA</span>
      <span class="presents">presents</span>
      <span class="main t1">Revelation</span>
      <span class="main t2">The Sanctuary</span>
      <span class="main t3">&amp; The Great</span>
      <span class="main t4">Deception</span>
    </h2>
    <div class="date-strip">May 19th - June 2nd, 2018</div>
  </div>
</section>

<div class="sheet-label" style="left:430px;top:598px">Inside</div>

<section class="spread spread--inside">
  <div class="photo" role="img" aria-label="Collage of a floating pyramid, standing stones and golden sanctuary furniture in a field at dusk" style="left:0;top:0;width:230px;height:340px;background:linear-gradient(180deg,#5f5780 0%,#bf8d86 35%,#d39a74 50%,#6f5b3a 75%,#4d4a2a 100%)"></div>
  <svg class="inside-shapes" width="720" height="555" viewBox="0 0 720 555" aria-hidden="true">
    <polygon points="200,0 720,0 720,200 200,340" fill="var(--charcoal)"/>
    <polygon points="0,334 720,196 720,208 0,348" fill="var(--yellow)"/>
    <polygon points="0,348 720,208 720,555 0,555" fill="#f8ece7"/>
  </svg>
  <div class="photo" role="img" aria-label="Dark silhouette of a giant figure" style="left:175px;top:0;width:110px;height:300px;background:linear-gradient(180deg,#3a3822,#2f2e22);border-radius:40px 40px 0 0;opacity:.9"></div>

  <h2 class="headline">GODS WAY IS IN<br>THE SANCTUARY.......</h2>
  <p class="subhead">THE BIBLE PROVIDES SOLID ANSWERS<br>TO ALL YOUR QUESTIONS</p>
  <p class="family-invite">We invite you to bring the whole family and discover<br>how Bible prophecy is relevant to our times.</p>

  <article class="session session--one">
    <div class="head"></div>
    <h5><b>OPENING</b> DAY!</h5>
    <p class="when">Saturday, May 19th - 11:00 a.m.</p>
    <div class="frame"></div>
    <div class="pic" role="img" aria-label="Painting of the four horsemen riding through fire" style="background:linear-gradient(160deg,#2b3a55,#7a2e1e 55%,#d0661f)"></div>
    <p class="label">Intro to<br>Revelation!</p>
  </article>
  <article class="session session--two">
    <div class="head"></div>
    <h5><b>NIGHT</b> SESSION</h5>
    <p class="when">Saturday, May 19th - 7:00 p.m.</p>
    <div class="frame"></div>
    <div class="pic" role="img" aria-label="Photo of a hand beside an ancient print pressed into stone" style="background:linear-gradient(150deg,#c9beb0,#a59a8c 60%,#8b7f72)"></div>
    <p class="label" style="top:152px">Ooparts!</p>
  </article>
  <article class="session session--three">
    <div class="head"></div>
    <h5><b>SUNDAY</b> NIGHT!</h5>
    <p class="when">Sunday, July 30th - 7:00 pm</p>
    <div class="frame"></div>
    <div class="pic" role="img" aria-label="Line drawing of a giant lying on the ground surrounded by tiny people" style="background:linear-gradient(160deg,#ffffff,#e6e6e6)"></div>
    <p class="label" style="top:152px">The Giants!</p>
  </article>

  <div class="speaker">
    <h3>Meet Our Speaker</h3>
    <p><i>Daniel Ashford</i> presents Daniel and Revelation with simple wisdom, understanding and vivid illustrations that all ages can comprehend. He believes by knowing the events outlined in God's word, will prepare people to stand in the last days, and help them avoid the pitfalls that Satan has laid for mankind. Prophecy lets us know where we came from and where we are going. So come out and hear God's final message to the last generation.</p>
  </div>

  <div class="feature" style="top:403px">INSPIRATIONAL<br>SINGING</div>
  <div class="feature" style="top:452px">NIGHTLY QUIZZES</div>
  <div class="feature" style="top:500px">HEALTH TOPICS</div>

  <div class="topics">
    <h4>FUTURE TOPICS</h4>
    <table>
      <tr>
        <td><b>Chariots of the Gods</b>Mon. May 21 - 7:00 p.m.</td>
        <td><b>Futurism</b>Sat. May 26 - 11:00 a.m.</td>
        <td><b>The Woman in Red</b>Tues. May 29 - 7:00 p.m.</td>
      </tr>
      <tr>
        <td><b>The Great Disappointment</b>Tues. May 22 - 7:00 p.m.</td>
        <td><b>Summary</b>Sat. May 26 - 7:00 p.m.</td>
        <td><b>Crying Loud In the Rain</b>Wed. May 30 - 7:00 p.m.</td>
      </tr>
      <tr>
        <td><b>Sanctuary Furniture</b>Wed. May 23 - 7:00 p.m.</td>
        <td><b>Final Deception</b>Sun. May 27 - 7:00 p.m.</td>
        <td><b>The Millennium</b>Fri. June 1 - 7:00 p.m.</td>
      </tr>
      <tr>
        <td><b>Israel, Evangelic &amp;<br>Sanctuary Rebuilding</b>Fri. May 25 - 7:00 p.m.</td>
        <td><b>Mark of the Beast &amp;<br>The 7 Last Plagues</b>Mon. May 28 - 7:00 p.m.</td>
        <td><b>The New Jerusalem</b>Sat. June 2 - 11:00 a.m.</td>
      </tr>
    </table>
  </div>
</section>

</body>
</html>
```